TARPLOAD business card design

TARPLOAD is a manufacturer of skip bags supplying both the domestic and commercial market. We wish to convey core characteristics of strength, professionalism and reliability to our customers. We are after a business card that uses our company colours of black and yellow as well as incorporating our logo. Our customers are predominantly in the construction or hardware industry. It is important the cards are professional as we are a small company wishing to appear larger than we actually are. more info on the company and product available at www.tarpload-example.com.au

Target Market(s)

hardware buyers, contruction company owners

Industry/Entity Type

Construction

Requirements
Must have
• company colours of black and yellow - No other colours or variation of yellow black. our company logo. card design must convey "tough"
• Card design must be landscape
• Details to be included on the card are:
• Name and Tiltle
• Phone number : 1300 41 62 53
• Mobile: 0452 718 903
• Fax: 03 9617 4852
• email: dale.hendry@tarpload-example.com.au
• address: PO Box 517, Kelvindale, VIC,3294
• Text in white when on a black background
Nice to have
• I like the idea of the back of the card being black with lighter circle area in the middle with black logo in the centre. Similar to the attached "iconic" card

```html
<!DOCTYPE html>
<html lang="en">
<head>
<meta charset="utf-8">
<title>TARPLOAD business card</title>
<link rel="stylesheet" href="https://fonts.googleapis.com/css2?family=Arimo:wght@400;700&display=swap">
<style>
  :root {
    --page: #ffffff;
    --yellow: #e8d30f;
    --black: #101010;
    --graphite: #5f686c;
    --white: #ffffff;
    --soft-white: #dcdcdc;
    --card-w: 774px;
    --card-h: 444px;
    --radius: 16px;
  }
  * { margin: 0; padding: 0; box-sizing: border-box; }
  html, body {
    width: 903px; height: 1200px; overflow: hidden;
    background: var(--page);
    font-family: "Arimo", Arial, sans-serif;
  }
  .card {
    position: absolute;
    width: var(--card-w); height: var(--card-h);
    border-radius: var(--radius);
    overflow: hidden;
    box-shadow: 0 3px 8px rgba(0,0,0,0.35);
  }
  .card-front { left: 61px; top: 132px; background: var(--yellow); }
  .card-back {
    left: 64px; top: 709px;
    background: radial-gradient(ellipse 48% 62% at 50% 44%, #7a8286 0%, #3e4447 45%, var(--black) 100%);
  }
  .front-shapes { position: absolute; inset: 0; width: 100%; height: 100%; }
  .website-front {
    position: absolute; left: 500px; top: 16px;
    font-size: 19px; color: var(--black); line-height: 1;
  }
  .person { position: absolute; left: 426px; top: 130px; color: var(--white); }
  .person-name { font-size: 28px; font-weight: 700; line-height: 1.2; }
  .person-title { font-size: 20px; font-weight: 700; line-height: 1.2; }
  .brand-name {
    position: absolute; font-weight: 700; color: var(--black);
    letter-spacing: 1px; line-height: 1;
  }
  .card-front .brand-name { left: 33px; top: 156px; font-size: 48px; }
  .contact-list {
    position: absolute; left: 33px; top: 266px;
    list-style: none; font-size: 21px; line-height: 30px; color: var(--black);
  }
  .card-back .brand-name {
    left: 0; right: 0; top: 200px; text-align: center; font-size: 62px;
  }
  .website-back {
    position: absolute; left: 0; right: 0; top: 374px;
    text-align: center; font-size: 22px; color: var(--soft-white);
  }
</style>
</head>
<body>
  <section class="card card-front">
    <svg class="front-shapes" viewBox="0 0 480 275" preserveAspectRatio="none" aria-hidden="true">
      <defs>
        <radialGradient id="panelGlow" cx="300" cy="150" r="190" gradientUnits="userSpaceOnUse">
          <stop offset="0" stop-color="var(--graphite)"/>
          <stop offset="0.55" stop-color="#2a2e30"/>
          <stop offset="1" stop-color="var(--black)"/>
        </radialGradient>
      </defs>
      <polygon points="162,0 290,0 305,30 480,30 480,275 377,275 312,158 250,158" fill="url(#panelGlow)"/>
      <line x1="176" y1="0" x2="259" y2="150" stroke="var(--yellow)" stroke-width="1.4"/>
      <line x1="184" y1="0" x2="266" y2="150" stroke="var(--yellow)" stroke-width="0.8"/>
      <line x1="405" y1="30" x2="480" y2="170" stroke="var(--yellow)" stroke-width="1.4"/>
      <line x1="414" y1="30" x2="480" y2="152" stroke="var(--yellow)" stroke-width="0.8"/>
    </svg>
    <p class="website-front">www.tarpload-example.com.au</p>
    <div class="person">
      <p class="person-name">Dale Hendry</p>
      <p class="person-title">Managing Director</p>
    </div>
    <p class="brand-name">TARPLOAD</p>
    <ul class="contact-list">
      <li>Phone: 1300 41 62 53</li>
      <li>Mobile: 0452 718 903</li>
      <li>Fax: 03 9617 4852</li>
      <li>e-mail: dale.hendry@tarpload-example.com.au</li>
      <li>Address: PO Box 517, Kelvindale, VIC, 3294</li>
    </ul>
  </section>

  <section class="card card-back">
    <p class="brand-name">TARPLOAD</p>
    <p class="website-back">www.tarpload-example.com.au</p>
  </section>
</body>
</html>
```